Need help in designing new business card utilizing our new logo.

Veltrix Solutions works with Construction Business Owners, Managers & IT Professionals to strengthen software usage and increase user productivity.

Our Construction Accounting and Mobile Field Management Software Clients engage with us in the following areas:

New Software Implementations
Software Re-Implementations
Redesigning Software Usage at the User Level
Project Coordination & Management
Continued Software Support

Old tag line:
Weighing Options - Implementing Solutions

www.veltrix-solutions.example

Quad Shift is a product, but not needed for a new business card.

```html
<!DOCTYPE html>
<html lang="en">
<head>
<meta charset="utf-8">
<title>Veltrix Solutions – Business Card</title>
<link rel="stylesheet" href="https://fonts.googleapis.com/css2?family=Montserrat:wght@700;800&family=Arimo:wght@400&display=swap">
<style>
  :root {
    --brand-blue: #2525b8;
    --text-grey: #8a8a8a;
    --card-grey: #7a7a7a;
    --card-white: #ffffff;
    --backdrop: #e7e5e6;
    --logo-mute: #c9c9c9;
  }
  * { box-sizing: border-box; margin: 0; padding: 0; }
  html, body { width: 1200px; height: 675px; overflow: hidden; }
  body {
    background: var(--backdrop);
    display: flex;
    align-items: center;
    justify-content: center;
    gap: 40px;
  }
  .card {
    width: 540px;
    height: 309px;
    position: relative;
    box-shadow: 0 6px 18px rgba(0,0,0,0.18);
  }
  .card--front { background: var(--card-white); }
  .card--back {
    background: var(--card-grey);
    display: flex;
    align-items: center;
    justify-content: center;
  }

  .brand {
    display: flex;
    align-items: center;
    gap: 12px;
  }
  .brand__mark {
    width: 34px; height: 34px;
    background: var(--brand-blue);
  }
  .brand__name {
    font-family: "Montserrat", sans-serif;
    font-weight: 800;
    font-size: 25px;
    color: var(--brand-blue);
    letter-spacing: 0.5px;
    white-space: nowrap;
  }
  .card--back .brand__name { color: var(--card-white); font-size: 30px; }
  .card--back .brand__mark { background: var(--brand-blue); width: 40px; height: 40px; }

  .card--front .brand {
    position: absolute;
    left: 26px;
    top: 136px;
  }
  .card--front .brand__name { font-size: 20px; }
  .card--front .brand__mark { width: 28px; height: 28px; }

  .divider {
    position: absolute;
    left: 268px;
    top: 58px;
    width: 1.5px;
    height: 196px;
    background: var(--brand-blue);
  }

  .contact {
    position: absolute;
    left: 288px;
    top: 62px;
    font-family: "Arimo", sans-serif;
    color: var(--text-grey);
  }
  .contact__name {
    font-family: "Montserrat", sans-serif;
    font-weight: 800;
    font-size: 19px;
    color: var(--brand-blue);
    text-transform: uppercase;
    letter-spacing: 0.3px;
  }
  .contact__role { font-size: 13px; margin-top: 2px; }
  .contact__address { font-size: 12.5px; line-height: 1.35; margin-top: 22px; }
  .contact__list { list-style: none; margin-top: 18px; font-size: 12.5px; }
  .contact__list li {
    display: flex;
    align-items: center;
    gap: 8px;
    margin-bottom: 6px;
  }
  .icon {
    width: 18px; height: 18px;
    border-radius: 50%;
    background: var(--brand-blue);
    display: flex;
    align-items: center;
    justify-content: center;
    flex-shrink: 0;
  }
  .icon svg { width: 11px; height: 11px; }
</style>
</head>
<body>
  <section class="card card--front" aria-label="Business card front">
    <div class="brand">
      <span class="brand__mark"></span>
      <span class="brand__name">Veltrix Solutions</span>
    </div>
    <span class="divider"></span>
    <div class="contact">
      <p class="contact__name">Dana R. Whitlock</p>
      <p class="contact__role">Owner</p>
      <p class="contact__address">14B Harbor Lane - Suite 310<br>Maple Falls NY 10000</p>
      <ul class="contact__list">
        <li>
          <span class="icon">
            <svg viewBox="0 0 24 24"><path fill="#fff" d="M6.6 10.8a15 15 0 0 0 6.6 6.6l2.2-2.2a1 1 0 0 1 1-.25 11.4 11.4 0 0 0 3.6.57 1 1 0 0 1 1 1V20a1 1 0 0 1-1 1A17 17 0 0 1 3 4a1 1 0 0 1 1-1h3.5a1 1 0 0 1 1 1c0 1.25.2 2.45.57 3.57a1 1 0 0 1-.25 1z"/></svg>
          </span>
          555-014-2286
        </li>
        <li>
          <span class="icon">
            <svg viewBox="0 0 24 24"><rect x="3" y="6" width="18" height="12" fill="none" stroke="#fff" stroke-width="2"/><path d="M3 6l9 7 9-7" fill="none" stroke="#fff" stroke-width="2"/></svg>
          </span>
          dwhitlock@veltrix-solutions.example
        </li>
        <li>
          <span class="icon">
            <svg viewBox="0 0 24 24" fill="none" stroke="#fff" stroke-width="2"><circle cx="12" cy="12" r="9"/><path d="M3 12h18M12 3c3 3 3 15 0 18M12 3c-3 3-3 15 0 18"/></svg>
          </span>
          www.veltrix-solutions.example
        </li>
      </ul>
    </div>
  </section>

  <section class="card card--back" aria-label="Business card back">
    <div class="brand">
      <span class="brand__mark"></span>
      <span class="brand__name">Veltrix Solutions</span>
    </div>
  </section>
</body>
</html>
```